i would like a business card to leave with customers and potential customers for electrical work and for the supply and install of reverse cycle airconditioning in the domestic and commercial market.
I own my own business and im a sole trader. I have an a'class electrical lisence and also a refrigeration lisence so i am
able to offer complete installations in airconditioning by a fully qualified and lisenced tradesman.
im looking for something that comes across as unique and professional.
i had the coluor black and some gold in mind but open to any coluors.
something like Beacon Electrical & Refrigeration
or Beacon Air.
i will use this design on a business card to advertise through summer to help generate installs through the busy season.

Target Market(s)

Mainly domestic house holds through summer who are in need of airconditioning and reliable information to acomadate thier cooling and heating requirements

Industry/Entity Type

Electrical

Requirements
Must have
• Business name- Beacon
My name- Peter Wollaston
My mobile no- 0457 819 302
My email- prwollaston@tarvel.com.au
Installation & Decomissioning of aiconditioning split systems
LIC NO: KTR 407516
Nice to have
• Beacon Electrical & Refrigeration

```html
<!DOCTYPE html>
<html lang="en">
<head>
<meta charset="utf-8">
<title>Beacon Electrical &amp; Refrigeration – Business Card</title>
<link href="https://fonts.googleapis.com/css2?family=Montserrat:wght@400;600;700&display=swap" rel="stylesheet">
<style>
  :root {
    --stage: #2e2e30;
    --brand-blue: #1fa6dc;
    --card-white: #ffffff;
    --ink: #1b1b1b;
    --watermark: #e9eef1;
    --badge-fill: #d6dde2;
  }
  * { margin: 0; padding: 0; box-sizing: border-box; }
  html, body {
    width: 1200px; height: 874px; overflow: hidden;
    background: var(--stage);
    font-family: "Montserrat", Arial, sans-serif;
  }
  .canvas { position: relative; width: 1200px; height: 874px; }

  .card {
    position: absolute; left: 280px; width: 640px; height: 366px;
    overflow: hidden; box-shadow: 0 10px 30px rgba(0,0,0,.45);
  }

  /* Front */
  .card-front { top: 46px; background: var(--card-white); }
  .front-top-band { position: absolute; left: 0; top: 0; width: 100%; height: 14px; background: var(--brand-blue); }
  .front-bottom-band {
    position: absolute; left: 0; bottom: 0; width: 100%; height: 50px;
    background: var(--brand-blue);
    color: var(--card-white); font-size: 17px; font-weight: 400; letter-spacing: .3px;
    display: flex; align-items: center; padding-left: 26px;
  }
  .front-watermark {
    position: absolute; left: 170px; top: 112px; width: 196px; height: 196px;
    border: 14px solid var(--watermark); border-radius: 50%;
  }
  .brand-lockup { position: absolute; left: 26px; top: 34px; display: flex; align-items: center; gap: 12px; z-index: 1; }
  .brand-dot { width: 58px; height: 58px; border: 5px solid var(--brand-blue); border-radius: 50%; flex: none; }
  .brand-name { color: var(--brand-blue); font-weight: 700; font-size: 38px; letter-spacing: 1px; line-height: 1; }
  .brand-sub { color: var(--ink); font-weight: 400; font-size: 13px; margin-top: 4px; }

  .contact { position: absolute; right: 46px; top: 128px; color: var(--ink); font-size: 14px; line-height: 1.45; z-index: 1; }
  .contact-name { color: var(--brand-blue); font-weight: 600; font-size: 19px; margin-bottom: 4px; }

  .partner-badge { position: absolute; left: 26px; bottom: 66px; width: 44px; height: 44px; }

  /* Back */
  .card-back {
    top: 462px; background: var(--brand-blue);
    display: flex; flex-direction: column; align-items: center; justify-content: center;
    color: var(--card-white);
  }
  .back-dot { width: 110px; height: 110px; border: 7px solid var(--card-white); border-radius: 50%; margin-bottom: 22px; }
  .back-name { font-weight: 700; font-size: 52px; letter-spacing: 2px; line-height: 1; }
  .back-sub { font-weight: 400; font-size: 16px; margin-top: 6px; }
</style>
</head>
<body>
<div class="canvas">

  <section class="card card-front">
    <div class="front-top-band"></div>
    <div class="front-watermark" aria-hidden="true"></div>

    <div class="brand-lockup">
      <div class="brand-dot" aria-hidden="true"></div>
      <div>
        <div class="brand-name">BEACON</div>
        <div class="brand-sub">Electrical &amp; Refrigeration</div>
      </div>
    </div>

    <div class="contact">
      <div class="contact-name">Peter Wollaston</div>
      <div>M: 0457 819 302</div>
      <div>E: prwollaston@tarvel.com.au</div>
      <div>LIC NO: KTR 407516</div>
    </div>

    <svg class="partner-badge" viewBox="0 0 44 44" role="img" aria-label="Accreditation badge placeholder">
      <rect x="0" y="0" width="44" height="44" fill="var(--badge-fill)"/>
    </svg>

    <div class="front-bottom-band">Installation &amp; Decomissioning of airconditioning split systems</div>
  </section>

  <section class="card card-back">
    <div class="back-dot" aria-hidden="true"></div>
    <div class="back-name">BEACON</div>
    <div class="back-sub">Electrical &amp; Refrigeration</div>
  </section>

</div>
</body>
</html>
```